Bold Creative Business Card for Digital Marketing Company (Contest)

NOTICE TO DESIGNERS: We understand this is how you make your living. Our commitment to you is to give you awesome and rapid feedback. If we don't think you are on the right track or have a chance of winning we will let you know right away so you don't have to focus your time with us and can continue to get work.

We respect the crowdsource community greatly. We have launched hundreds of crowdsource projects and will make this a great experience for you if you choose to participate (we hope you will!)

--------------
Brief
-------------

We are a cutting edge digital marketing company and we need a new, bold and creative business card designed to reflect who we are and what we do. We want our brand to stand out and be noticed.

The name of our company is: Tundrel Web Marketing

Definition of Tundrel:

a. a person pursuing rebellious, even potentially disruptive, policies or ideas:

b. a lone dissenter, as an intellectual, an artist, or a politician, who takes an independent stand apart from his or her associates

c. unorthodox, unconventional, nonconformist

Our businesses is helping small to medium size businesses with their online marketing using bold and creative outside the box strategies that get results.

We are an industry leader and need our business cards to stand out when we hand them out to people, and to be amazing so we stand out and "lead the pack"!

Our current website: http://www.tundrelwebmarketing.example

We are rebranding our site to reflect the new logo we just got but you will at least have an idea of who we are and what we do.

Colors We Want: We would like to see burnt Orange, Dark Blue, Gray and/or Black.

We need a front and back designed!

Be creative! Even to the point of creative-shaped business cards. Think outside the box. Let nothing stop your imagination! At the very least, we know that we want business cards that are not the US Standard 2"x3.5"... but rather the wider 3.35"x2.17" (European Standard) with rounded corners if you want to stick with a rectangular shape.

On the front we need:

Our Logo
Place for a name ie Dale Voskuij
Place for our phone number (505) 555 - 7680
Place for email name@tundrelwebmarketing.example
Place for our website www.TundrelWebMarketing.example

Optional... Place for a headshot photo of the person who the business card will be used for

On the back we need:

The wording... FREE VIDEO SERIES! "9 Quick Moves To Grow Your Company This Week!" www.TundrelWebMarketing.example/SmartIdeas

We are excited to see what you come up with.

Thank you for your interests and for participating in this contest!
Updates

Hi everyone! Thanks for all your submissions. However, we feel that most of you are "missing" what we're looking for. Almost all of the designs that have come in are what we would call "standard", "generic", or "typical". We are looking for something creative, different, attention-getting, a business card that would stand out amongst a stack of other business cards. I've shot this video: http://clipvault.example/t/qPzTbw4hYcs Please take the time to review it. Let us know if you have questions. Thanks!

Target Market(s)

Our target market is small to medium sized business owners who need help with their online marketing.

Industry/Entity Type

Marketing

Font styles to use
Sans Serif

Colors
0355a3
85acd3
f78f20
f37022
faa54b
f68d4d

Requirements
Must have
• On the front we need:

Our Logo

Be CREATIVE! INTERESTING!

On the back we need:

Use the colors from our logo!
Nice to have
• Optional... Place for a headshot photo of the person who the business card will be used for.
Should not have
• Boring, "traditional" look and feel. We want and need to stand out!

```html
<!DOCTYPE html>
<html lang="en">
<head>
<meta charset="utf-8">
<title>Tundrel Web Marketing – Business Card</title>
<link rel="stylesheet" href="https://fonts.googleapis.com/css2?family=Carlito:wght@400;700&family=Didact+Gothic&display=swap">
<style>
  :root {
    --page: #1c1c1e;
    --card: #0a0a0b;
    --card-edge: #202124;
    --orange: #f78f20;
    --orange-deep: #f37022;
    --blue: #0355a3;
    --blue-light: #2a8fd6;
    --blue-pale: #85acd3;
    --white: #f4f4f4;
    --grey: #a9a9ad;
  }
  * { box-sizing: border-box; margin: 0; padding: 0; }
  html, body { width: 1200px; height: 965px; overflow: hidden; }
  body {
    background: var(--page);
    font-family: "Carlito", "Calibri", sans-serif;
    color: var(--white);
    display: flex;
    align-items: center;
    justify-content: center;
    gap: 50px;
  }
  .card {
    position: relative;
    width: 540px;
    height: 350px;
    border-radius: 26px;
    background: var(--card);
    border: 1px solid var(--card-edge);
    overflow: hidden;
  }

  /* Front */
  .brand {
    position: absolute;
    left: 40px;
    top: 38px;
    display: flex;
    align-items: center;
    gap: 12px;
    font-size: 26px;
    font-weight: 400;
    letter-spacing: 1px;
    color: var(--white);
  }
  .brand-dot {
    width: 16px; height: 16px;
    background: var(--orange);
  }
  .headshot {
    position: absolute;
    right: 40px;
    top: 60px;
    width: 132px;
    height: 108px;
    border-radius: 12px;
    border: 3px solid var(--blue-light);
    background: linear-gradient(160deg, #7fb2d9 0%, #b9c9d6 45%, #c79a7d 100%);
  }
  .person {
    position: absolute;
    right: 40px;
    top: 180px;
    text-align: right;
  }
  .person-name {
    font-size: 22px;
    font-weight: 700;
    color: var(--orange);
  }
  .person-role {
    font-size: 16px;
    color: var(--white);
  }
  .contact {
    position: absolute;
    right: 40px;
    top: 240px;
    list-style: none;
    text-align: right;
    font-size: 14px;
  }
  .contact li {
    display: flex;
    align-items: center;
    justify-content: flex-end;
    gap: 8px;
    margin-bottom: 6px;
  }
  .contact svg { width: 16px; height: 16px; }
  .wave {
    position: absolute;
    left: 0; bottom: 0;
    width: 540px; height: 110px;
  }
  .site {
    position: absolute;
    left: 34px;
    bottom: 22px;
    font-size: 16px;
    color: var(--white);
  }

  /* Back */
  .promo {
    position: absolute;
    left: 60px;
    top: 110px;
    right: 40px;
  }
  .promo-head {
    font-size: 24px;
    font-weight: 700;
    color: var(--orange);
    margin-bottom: 10px;
    text-align: right;
    padding-right: 30px;
  }
  .promo-line {
    font-family: "Didact Gothic", "Century Gothic", sans-serif;
    font-size: 20px;
    color: var(--white);
    margin-bottom: 26px;
  }
  .promo-url {
    font-size: 17px;
    color: var(--white);
  }
  .promo-url .accent { color: var(--orange); }
  .promo-rule {
    display: block;
    margin-top: 14px;
    height: 1px;
    width: 420px;
    background: linear-gradient(90deg, transparent, var(--grey));
  }
</style>
</head>
<body>

<section class="card card-front" aria-label="Card front">
  <div class="brand"><span class="brand-dot"></span>Tundrel Web Marketing</div>

  <div class="headshot" role="img" aria-label="Headshot photo of the card holder"></div>

  <div class="person">
    <p class="person-name">Dale Voskuij</p>
    <p class="person-role">Job Title</p>
  </div>

  <ul class="contact">
    <li>(505) 555 - 7680
      <svg viewBox="0 0 16 16" aria-hidden="true"><circle cx="8" cy="8" r="7" fill="none" stroke="var(--orange)" stroke-width="1.6"/><path d="M5.5 4.5l1.5 0 .7 1.8-1 .8a5 5 0 0 0 2.2 2.2l.8-1 1.8.7v1.5a1 1 0 0 1-1 1A6 6 0 0 1 4.5 5.5a1 1 0 0 1 1-1z" fill="var(--orange)"/></svg>
    </li>
    <li>name@tundrelwebmarketing.example
      <svg viewBox="0 0 16 16" aria-hidden="true"><circle cx="8" cy="8" r="7" fill="none" stroke="var(--orange)" stroke-width="1.6"/><rect x="4.2" y="5.3" width="7.6" height="5.4" rx="0.8" fill="var(--orange)"/><path d="M4.4 5.6L8 8.4l3.6-2.8" fill="none" stroke="var(--card)" stroke-width="0.9"/></svg>
    </li>
  </ul>

  <svg class="wave" viewBox="0 0 540 110" preserveAspectRatio="none" aria-hidden="true">
    <defs>
      <linearGradient id="blueBand" x1="0" y1="0" x2="1" y2="0">
        <stop offset="0" stop-color="var(--blue-light)"/>
        <stop offset="1" stop-color="var(--blue)"/>
      </linearGradient>
    </defs>
    <path d="M0 8 C120 10 270 40 400 110 L0 110 Z" fill="var(--orange)"/>
    <path d="M0 26 C130 26 270 58 370 110 L0 110 Z" fill="url(#blueBand)"/>
  </svg>
  <p class="site">www.TundrelWebMarketing.example</p>
</section>

<section class="card card-back" aria-label="Card back">
  <div class="promo">
    <p class="promo-head">FREE VIDEO SERIES!</p>
    <p class="promo-line">9 Quick Moves To Grow Your Company This Week!</p>
    <p class="promo-url">www.<span class="accent">TundrelWebMarketing</span>.example/SmartIdeas</p>
    <span class="promo-rule"></span>
  </div>
</section>

</body>
</html>
```